Business cards design on a high standard

We advise clients on insurance and financial matters, since these clients pay for our advice, the design should have a high standard. Our logo should be included. From the colors we are open for everything.

Colors

Designer to choose colors to be used in the design.

```html
<!DOCTYPE html>
<html lang="en">
<head>
<meta charset="utf-8">
<title>Alpine Counsel — Business Cards</title>
<link rel="stylesheet" href="https://fonts.googleapis.com/css2?family=Montserrat:wght@800&family=Roboto:wght@400;500&display=swap">
<style>
  :root {
    --brand-red: #e10600;
    --band-grey: #9a9a9e;
    --paper-white: #ffffff;
    --ink-dark: #2b2b2b;
    --stage: #3a3a3c;
    --stage-light: #4a4a4c;
  }
  * { box-sizing: border-box; margin: 0; padding: 0; }
  html, body { width: 1200px; height: 900px; overflow: hidden; }
  body {
    background: radial-gradient(circle at 50% 45%, var(--stage-light), var(--stage) 70%);
    font-family: "Roboto", Arial, sans-serif;
    position: relative;
  }
  .card {
    position: absolute;
    top: 301px;
    width: 520px;
    height: 298px;
    background: var(--brand-red);
    overflow: hidden;
    box-shadow: 0 14px 30px rgba(0,0,0,0.45);
  }
  .card--front { left: 60px; }
  .card--back { left: 620px; }

  .card__swoosh { position: absolute; inset: 0; width: 100%; height: 100%; }

  .brand-name {
    font-family: "Montserrat", Arial, sans-serif;
    font-weight: 800;
    color: var(--paper-white);
    text-transform: uppercase;
    line-height: 0.95;
    letter-spacing: 1px;
  }
  .card--front .brand-name {
    position: absolute;
    left: 28px;
    top: 26px;
    font-size: 30px;
  }
  .card--back .brand-name {
    position: absolute;
    left: 0;
    right: 0;
    top: 100px;
    text-align: center;
    font-size: 50px;
  }
  .brand-name span { display: block; }
  .card--front .brand-name span + span { font-size: 19px; letter-spacing: 3px; }
  .card--back .brand-name span + span { font-size: 31px; letter-spacing: 6px; }

  .holder {
    position: absolute;
    right: 26px;
    top: 58px;
    text-align: right;
    color: var(--paper-white);
  }
  .holder__name {
    font-size: 21px;
    font-weight: 500;
    text-transform: uppercase;
    letter-spacing: 0.5px;
  }
  .holder__role { font-size: 14px; margin-top: 2px; }

  .contact {
    position: absolute;
    right: 172px;
    bottom: 16px;
    list-style: none;
    text-align: right;
    color: var(--ink-dark);
    font-size: 13px;
    line-height: 18px;
  }
  .contact li { display: flex; justify-content: flex-end; align-items: center; gap: 6px; }
  .contact .address { padding-right: 17px; }
  .contact svg { width: 11px; height: 11px; flex: none; }
  .contact .web-accent { color: var(--brand-red); }

  .back-web {
    position: absolute;
    left: 118px;
    top: 232px;
    color: var(--paper-white);
    font-size: 13px;
    letter-spacing: 0.3px;
  }
</style>
</head>
<body>

  <article class="card card--front" aria-label="Business card front">
    <svg class="card__swoosh" viewBox="0 0 520 298" preserveAspectRatio="none" aria-hidden="true">
      <path d="M0,112 C300,92 480,122 500,298 L0,298 Z" fill="var(--paper-white)"/>
      <path d="M0,120 C300,100 470,130 490,298 L0,298 Z" fill="var(--band-grey)"/>
      <path d="M0,160 C300,140 430,170 440,298 L0,298 Z" fill="var(--paper-white)"/>
    </svg>

    <div class="brand-name"><span>Alpine</span><span>Counsel</span></div>

    <div class="holder">
      <div class="holder__name">Daniel Reyes</div>
      <div class="holder__role">Director</div>
    </div>

    <ul class="contact">
      <li class="address">1187 Larkspur Lane</li>
      <li class="address">Corvallis, OR 97330</li>
      <li><span>555 012-3478</span>
        <svg viewBox="0 0 12 12"><path d="M3 1 L5 3.5 L4 5 C4.8 6.6 5.6 7.4 7 8 L8.5 7 L11 9 L9.5 11 C5 10.5 1.5 7 1 2.5 Z" fill="var(--brand-red)"/></svg>
      </li>
      <li><span>info@alpinecounsel.com</span>
        <svg viewBox="0 0 12 12"><rect x="0.5" y="2" width="11" height="8" fill="var(--brand-red)"/><path d="M1 2.5 L6 6.5 L11 2.5" stroke="#fff" stroke-width="1" fill="none"/></svg>
      </li>
      <li><span>www.<span class="web-accent">alpinecounsel</span>.com</span>
        <svg viewBox="0 0 12 12"><circle cx="6" cy="6" r="5.5" fill="var(--brand-red)"/><path d="M0.5 6 H11.5 M6 0.5 V11.5 M2 3 H10 M2 9 H10" stroke="#fff" stroke-width="0.7"/><ellipse cx="6" cy="6" rx="2.5" ry="5.5" stroke="#fff" stroke-width="0.7" fill="none"/></svg>
      </li>
    </ul>
  </article>

  <article class="card card--back" aria-label="Business card back">
    <div class="brand-name"><span>Alpine</span><span>Counsel</span></div>
    <div class="back-web">www.alpinecounsel.com</div>
  </article>

</body>
</html>
```